STI/STD Medical Clinic- Wellspring Crest Partners, Inc Website

We are a STI clinic in florida looking for a website. We want to be professional but also playful. We want a buildout similar to the website listed below as our clinic is very similar to theirs.

This is a great example of a clinic doing similar stuff as us. We obviously do not want their color scheme but their format and buildout work. Please see our logo attached for color schemes etc.

https://bluefernclinicmiami.org

Industry/Entity Type

Medical

Coding

Coded - Design and coding required

Number of Pages Required

5+ page

Font styles to use
Sans Serif

```html
<!DOCTYPE html>
<html lang="en">
<head>
<meta charset="utf-8">
<title>Wellspring Crest Partners — STI/STD Medical Clinic</title>
<link href="https://fonts.googleapis.com/css2?family=Poppins:wght@400;500;600;700;800&family=Roboto:wght@400;500;700&display=swap" rel="stylesheet">
<style>
:root{
  --pink:#ec2f6b;
  --magenta:#c7307e;
  --purple:#6d3aa6;
  --violet:#8e44ad;
  --coral:#f04e3e;
  --orange:#f36a2f;
  --ink:#16161f;
  --text:#55555f;
  --muted:#8a8a95;
  --line:#e6e1ec;
  --white:#fff;
  --soft:#f7f3fa;
  --grad:linear-gradient(90deg,var(--pink),var(--purple));
}
*{box-sizing:border-box;margin:0;padding:0}
html,body{width:1200px;height:4416px;overflow:hidden}
body{font-family:"Roboto",Arial,sans-serif;color:var(--ink);background:var(--white);position:relative}
h1,h2,h3,h4,.nav,.btn{font-family:"Poppins",Arial,sans-serif}
.abs{position:absolute}
.ph{display:block}

/* header */
.site-header{position:absolute;top:0;left:0;width:1200px;height:56px;background:var(--white);display:flex;align-items:center;padding:0 40px;z-index:3;box-shadow:0 2px 10px rgba(0,0,0,.06)}
.brand{display:flex;align-items:center;gap:8px;font-family:"Poppins",sans-serif;font-weight:700;font-size:17px;color:var(--purple)}
.brand .dot{width:20px;height:20px;border-radius:50%;background:var(--pink)}
.nav{margin-left:auto;display:flex;gap:28px;font-size:11px;font-weight:600;color:var(--ink);align-items:center}
.nav span.active{color:var(--pink)}
.search{width:110px;height:24px;border:1px solid var(--line);border-radius:12px;display:flex;align-items:center;justify-content:flex-end;padding-right:8px;margin-left:18px}

/* hero */
.hero{position:absolute;top:0;left:0;width:1200px;height:720px;overflow:hidden}
.hero-photo{position:absolute;inset:0;background:linear-gradient(100deg,#c9b5b8 0%,#d8cdd0 40%,#ece8e6 70%,#c8d2cf 100%)}
.hero-overlay{position:absolute;inset:0;background:linear-gradient(90deg,rgba(109,58,166,.55) 0%,rgba(236,47,107,.35) 45%,rgba(255,255,255,0) 70%)}
.hero-text{position:absolute;left:80px;top:280px;width:560px;color:var(--white)}
.hero-text .kicker{font-size:18px;margin-bottom:14px}
.hero-text h1{font-size:42px;line-height:1.18;font-weight:700;margin-bottom:18px}
.hero-text p{font-size:15px;line-height:1.45;max-width:450px;margin-bottom:30px}
.btn{display:inline-flex;align-items:center;gap:8px;border-radius:4px;font-size:11px;font-weight:600}
.btn-pink{background:var(--pink);color:var(--white);padding:9px 16px}

/* features */
.features{position:absolute;top:720px;left:228px;display:flex;gap:24px;z-index:2}
.feature{width:232px;height:190px;background:var(--white);border-radius:8px;box-shadow:0 6px 24px rgba(60,20,80,.12);text-align:center;padding:22px 16px 0;border-bottom:4px solid var(--pink)}
.feature .ico{width:48px;height:48px;margin:0 auto 12px}
.feature h3{font-size:14px;font-weight:600;margin-bottom:6px}
.feature p{font-size:10px;color:var(--text);line-height:1.4;margin-bottom:14px}
.pill{display:inline-block;border:1px solid #ccc;border-radius:12px;padding:4px 14px;font-size:9px;font-weight:600;color:var(--ink)}

/* about */
.about{position:absolute;top:980px;left:0;width:1200px;height:420px}
.about-photo{position:absolute;left:40px;top:0;width:500px;height:400px;background:linear-gradient(135deg,#dfe6ee,#9fb5c9 55%,#5d7ea6);border-radius:2px}
.about-body{position:absolute;left:588px;top:10px;width:560px}
.section-icon{width:26px;height:26px;margin-bottom:6px}
.about-body h2{font-size:32px;font-weight:700;margin-bottom:24px}
.about-body h3{font-size:22px;font-weight:600;margin-bottom:10px}
.about-body .lead{font-size:17px;line-height:1.4;margin-bottom:18px}
.ticks{list-style:none}
.ticks li{display:flex;align-items:center;gap:14px;font-size:14px;color:var(--text);margin-bottom:14px}
.ticks li::before{content:"";width:14px;height:14px;border-radius:50%;background:var(--pink);flex:none}

/* services */
.services{position:absolute;top:1420px;left:0;width:1200px;height:600px;background:var(--white)}
.center-title{text-align:center;font-size:30px;font-weight:700}
.svc{position:absolute;width:360px}
.svc h4{font-size:15px;font-weight:600;margin-bottom:4px}
.svc p{font-size:11px;color:var(--text);line-height:1.45}
.svc.left{text-align:right}
.svc .si{position:absolute;top:0;width:40px;height:40px}
.svc.left .si{right:-56px}
.svc.right .si{left:-56px}
.wheel{position:absolute;left:450px;top:170px;width:300px;height:300px;border-radius:50%;background:radial-gradient(circle,#fde9f1 0%,#f1e6f8 55%,#fff 72%)}

/* doctors */
.doctors{position:absolute;top:2040px;left:0;width:1200px;height:760px}
.doctors .sub{text-align:center;font-size:12px;color:var(--text);width:440px;margin:8px auto 0;line-height:1.4}
.doc-grid{position:absolute;top:160px;left:140px;display:grid;grid-template-columns:repeat(4,200px);column-gap:40px;row-gap:22px}
.doc{height:278px;border:3px solid transparent;border-radius:6px;background:linear-gradient(var(--white),var(--white)) padding-box,linear-gradient(160deg,var(--pink),var(--purple)) border-box;padding:14px 12px 0;text-align:center;position:relative}
.doc .face{width:96px;height:96px;margin:0 auto 10px;border-radius:50%;background:linear-gradient(160deg,#e8eef4,#b9c8d8)}
.doc h4{font-size:14px;font-weight:600}
.doc .role{font-size:11px;color:var(--pink);margin:2px 0 8px}
.doc p{font-size:9px;color:var(--text);line-height:1.4}
.doc .more{position:absolute;right:12px;bottom:8px;font-size:9px;font-weight:700}

/* news */
.news{position:absolute;top:2860px;left:0;width:1200px;height:760px;background:linear-gradient(110deg,var(--pink) 0%,#e0467c 45%,#b04595 100%);color:var(--white);text-align:center}
.news h2{font-size:34px;font-weight:700;margin-top:80px}
.news .sub{font-size:16px;width:620px;margin:6px auto 0;line-height:1.4}
.news-grid{position:absolute;top:220px;left:150px;display:grid;grid-template-columns:repeat(3,260px);column-gap:40px}
.news-img{height:260px;border-radius:2px}
.news-item h3{font-size:24px;font-weight:700;margin:22px 0 10px}
.news-item p{font-size:12px;line-height:1.45;width:230px;margin:0 auto 12px}
.news-item .rm{font-size:12px;font-weight:700}

/* appointment */
.appointment{position:absolute;top:3660px;left:0;width:1200px;height:540px}
.appt-photo{position:absolute;left:0;top:0;width:580px;height:540px;background:linear-gradient(120deg,#f2efe9,#d9d3cb 50%,#b7b0a9)}
.appt-card{position:absolute;left:580px;top:10px;width:560px;height:470px;background:var(--white);border:1px solid var(--line);box-shadow:0 8px 30px rgba(60,20,80,.1);padding:32px 34px}
.appt-card .label{font-size:13px;color:var(--pink);margin-bottom:6px}
.appt-card h2{font-size:36px;font-weight:700;margin-bottom:42px}
.fields{display:grid;grid-template-columns:1fr 1fr;column-gap:26px;row-gap:30px}
.field{display:flex;align-items:center;gap:12px;border-bottom:1px solid #cfcad6;padding-bottom:10px;font-size:13px;color:var(--ink)}
.field .fi{width:30px;height:30px;border-radius:50%;background:var(--soft);flex:none}
.appt-card .btn{margin:50px auto 0;display:flex;width:180px;justify-content:center;background:var(--grad);color:var(--white);padding:12px 0;border-radius:20px}
.corner{position:absolute;right:-1px;top:-1px}

/* footer */
.site-footer{position:absolute;top:4200px;left:0;width:1200px;height:216px;background:linear-gradient(90deg,var(--coral),var(--orange) 50%,var(--coral));color:var(--white)}
.foot-cols{position:absolute;top:22px;left:40px;display:grid;grid-template-columns:300px 230px 180px 220px 200px;column-gap:0}
.foot-brand .brand{color:var(--white);margin-bottom:10px}
.foot-brand .brand .dot{background:var(--white)}
.foot-brand p{font-size:10px;line-height:1.45;width:260px}
.foot-cols h4{font-size:20px;font-weight:700;margin-bottom:10px}
.foot-cols ul{list-style:none;font-size:10px;line-height:1.8}
.foot-cols ul li::before{content:"• "}
.contact li::before{content:"" !important}
.contact li{display:flex;gap:8px;align-items:center}
.contact i{width:14px;height:14px;border-radius:50%;background:rgba(255,255,255,.85);display:inline-block}
.socials{display:flex;gap:8px;margin-top:10px}
.socials span{width:16px;height:16px;border-radius:50%;border:1px solid var(--white)}
.copyright{position:absolute;bottom:0;left:0;width:100%;height:30px;border-top:1px solid rgba(255,255,255,.35);font-size:10px;display:flex;align-items:center;justify-content:center}
</style>
</head>
<body>

<section class="hero">
  <div class="hero-photo" role="img" aria-label="Smiling female doctor with stethoscope and an older patient in a bright clinic"></div>
  <div class="hero-overlay"></div>
  <div class="hero-text">
    <p class="kicker">Welcome to Wellspring Crest Partners</p>
    <h1>We solve problems on every level of treatment</h1>
    <p>Lorem ipsum dolor sit amet, consectetur adipiscing elit, sed do eiusmod tempor incididunt ut labore magna.</p>
    <span class="btn btn-pink">Get Appointment</span>
  </div>
</section>

<header class="site-header">
  <div class="brand"><span class="dot"></span>Wellspring Crest</div>
  <nav class="nav">
    <span class="active">HOME</span><span>ABOUT US ▾</span><span>MEET THE TEAM ▾</span><span>SERVICES ▾</span><span>NEWS ▾</span><span>FAQs ▾</span><span>CONTACT US ▾</span>
    <span class="search"><svg width="11" height="11" viewBox="0 0 12 12"><circle cx="5" cy="5" r="4" fill="none" stroke="#888" stroke-width="1.5"/><path d="M8 8l3 3" stroke="#888" stroke-width="1.5"/></svg></span>
  </nav>
</header>

<div class="features">
  <div class="feature">
    <svg class="ico" viewBox="0 0 48 48"><path d="M24 4l16 6v12c0 11-7 18-16 22C15 40 8 33 8 22V10z" fill="none" stroke="var(--pink)" stroke-width="3"/><path d="M24 31s-8-5-8-10a4 4 0 018-1 4 4 0 018 1c0 5-8 10-8 10z" fill="var(--purple)"/></svg>
    <h3>With greate care!</h3>
    <p>Lorem ipsum dolor sit amet, consectetur adipiscing elit. Accumsan felis tempus nascetur.</p>
    <span class="pill">Read More ›</span>
  </div>
  <div class="feature">
    <svg class="ico" viewBox="0 0 48 48"><circle cx="24" cy="24" r="19" fill="none" stroke="var(--pink)" stroke-width="3"/><text x="24" y="29" text-anchor="middle" font-family="Poppins,sans-serif" font-weight="700" font-size="14" fill="var(--purple)">24</text></svg>
    <h3>24 Hours Care Service</h3>
    <p>Lorem ipsum dolor sit amet, consectetur adipiscing elit. Accumsan felis tempus nascetur.</p>
    <span class="pill">Read More ›</span>
  </div>
  <div class="feature">
    <svg class="ico" viewBox="0 0 48 48"><rect x="4" y="14" width="26" height="20" rx="2" fill="none" stroke="var(--pink)" stroke-width="3"/><path d="M30 20h8l6 7v7H30z" fill="none" stroke="var(--purple)" stroke-width="3"/><circle cx="13" cy="37" r="4" fill="var(--purple)"/><circle cx="36" cy="37" r="4" fill="var(--purple)"/><path d="M17 19v10M12 24h10" stroke="var(--pink)" stroke-width="3"/></svg>
    <h3>All Time Ambulance Help</h3>
    <p>Lorem ipsum dolor sit amet, consectetur adipiscing elit. Accumsan felis tempus nascetur.</p>
    <span class="pill">Read More ›</span>
  </div>
</div>

<section class="about">
  <div class="about-photo" role="img" aria-label="Team of doctors reviewing an x-ray together"></div>
  <div class="about-body">
    <svg class="section-icon" viewBox="0 0 26 26"><rect x="9" y="1" width="8" height="24" fill="var(--pink)"/><rect x="1" y="9" width="24" height="8" fill="var(--purple)"/></svg>
    <h2>About Us</h2>
    <h3>Complete Medical Solution in One Place</h3>
    <p class="lead">Lorem ipsum dolor sit amet, consectetur adipiscing elit. Ipsum ipsum amet felis leo ipsum gravida nulla faucibus sit. consectetur adipiscing elit. Ipsum quis amet felis</p>
    <ul class="ticks">
      <li>Lorem ipsum dolor sit amet, consectetur adipiscing elit.</li>
      <li>It has survived not only five centuries</li>
      <li>The point of using Lorem Ipsum is that it has a more</li>
      <li>Lorem ipsum dolor sit amet, consectetur adipiscing elit.</li>
      <li>Lorem ipsum dolor sit amet, consectetur adipiscing elit.</li>
    </ul>
  </div>
</section>

<svg class="abs" style="top:1410px;left:0" width="1200" height="70" viewBox="0 0 1200 70">
  <defs><linearGradient id="bandG" x1="0" x2="1"><stop offset="0" stop-color="#6d3aa6"/><stop offset=".5" stop-color="#ec2f6b"/><stop offset="1" stop-color="#6d3aa6"/></linearGradient></defs>
  <path d="M0 0H1200V14L600 44L0 14Z" fill="url(#bandG)"/>
  <path d="M0 14L600 44L0 30Z" fill="#ec2f6b" opacity=".5"/>
</svg>

<section class="services">
  <svg class="abs" style="left:586px;top:56px" width="28" height="28" viewBox="0 0 26 26"><rect x="9" y="1" width="8" height="24" fill="var(--pink)"/><rect x="1" y="9" width="24" height="8" fill="var(--purple)"/></svg>
  <h2 class="center-title" style="margin-top:86px">Our Best Services</h2>
  <svg class="abs" style="left:340px;top:104px" width="520" height="30" viewBox="0 0 520 30"><path d="M0 4H90L110 26H0z" fill="var(--pink)"/><path d="M520 4H430L410 26H520z" fill="var(--purple)"/></svg>
  <div class="wheel" role="img" aria-label="Circular medical illustration of cells and molecules around a 24-hour care emblem"></div>

  <div class="svc left" style="left:56px;top:180px"><svg class="si" viewBox="0 0 40 40"><rect x="12" y="6" width="16" height="28" rx="4" fill="none" stroke="var(--pink)" stroke-width="3"/><path d="M16 14h8" stroke="var(--purple)" stroke-width="3"/></svg><h4>Hepatitis C Medical Care</h4><p>It is a long established fact that a reader will<br>be distracted by the readable.</p></div>
  <div class="svc left" style="left:56px;top:300px"><svg class="si" viewBox="0 0 40 40"><circle cx="20" cy="20" r="14" fill="none" stroke="var(--pink)" stroke-width="3"/><path d="M13 20h14M20 13v14" stroke="var(--purple)" stroke-width="3"/></svg><h4>PrEP</h4><p>There are many variations of passages of<br>Lorem ipsum available.</p></div>
  <div class="svc left" style="left:56px;top:440px"><svg class="si" viewBox="0 0 40 40"><rect x="6" y="10" width="28" height="22" rx="3" fill="none" stroke="var(--pink)" stroke-width="3"/><path d="M15 10V6h10v4" fill="none" stroke="var(--purple)" stroke-width="3"/></svg><h4>Case Management (Non-Medical)</h4><p>It is a long established fact that a reader will<br>be distracted by the readable.</p></div>

  <div class="svc right" style="left:788px;top:180px"><svg class="si" viewBox="0 0 40 40"><path d="M20 34s-13-8-13-17a7 7 0 0113-3 7 7 0 0113 3c0 9-13 17-13 17z" fill="none" stroke="var(--pink)" stroke-width="3"/></svg><h4>HIV Medical Care</h4><p>It is a long established fact that a reader will<br>be distracted by the readable.</p></div>
  <div class="svc right" style="left:788px;top:300px"><svg class="si" viewBox="0 0 40 40"><path d="M10 30L30 10M14 12l14 14" stroke="var(--pink)" stroke-width="3"/><circle cx="20" cy="20" r="15" fill="none" stroke="var(--purple)" stroke-width="2"/></svg><h4>STI Testing and Treatment</h4><p>There are many variations of passages of<br>Lorem ipsum available.</p></div>
  <div class="svc right" style="left:788px;top:440px"><svg class="si" viewBox="0 0 40 40"><rect x="4" y="12" width="22" height="16" rx="2" fill="none" stroke="var(--pink)" stroke-width="3"/><path d="M26 16h6l4 6v6H26" fill="none" stroke="var(--purple)" stroke-width="3"/><circle cx="12" cy="31" r="3" fill="var(--purple)"/><circle cx="31" cy="31" r="3" fill="var(--purple)"/></svg><h4>Transportation Services</h4><p>Many desktop publishing packages and<br>web page editors.</p></div>
</section>

<svg class="abs" style="top:1990px;left:0" width="1200" height="40" viewBox="0 0 1200 40"><path d="M0 0L1200 30V40H0z" fill="var(--pink)" opacity=".18"/><path d="M0 20L1200 0V6L0 28z" fill="var(--purple)" opacity=".35"/></svg>

<section class="doctors">
  <svg class="abs" style="left:586px;top:20px" width="28" height="28" viewBox="0 0 26 26"><rect x="9" y="1" width="8" height="24" fill="var(--pink)"/><rect x="1" y="9" width="24" height="8" fill="var(--purple)"/></svg>
  <h2 class="center-title" style="margin-top:56px">Meet Our Qualified Doctors</h2>
  <p class="sub">Lorem ipsum dolor sit amet, consectetur adipiscing elit, sed do eiusmod tempor incididunt ut labore et dolore magna aliqua.</p>
  <div class="doc-grid">
    <div class="doc"><div class="face" role="img" aria-label="Doctor portrait"></div><h4>Lorem ipsum</h4><p class="role">Cardiologist</p><p>Lorem ipsum dolor sit amet, consectetur adipiscing elit. Accumsan felis tempus nascetur.</p><span class="more">Read More</span></div>
    <div class="doc"><div class="face" role="img" aria-label="Doctor portrait"></div><h4>Lorem ipsum</h4><p class="role">Nephrologists</p><p>Lorem ipsum dolor sit amet, consectetur adipiscing elit. Accumsan felis tempus nascetur.</p><span class="more">Read More</span></div>
    <div class="doc"><div class="face" role="img" aria-label="Doctor portrait"></div><h4>Lorem ipsum</h4><p class="role">Dermatologist</p><p>Lorem ipsum dolor sit amet, consectetur adipiscing elit. Accumsan felis tempus nascetur.</p><span class="more">Read More</span></div>
    <div class="doc"><div class="face" role="img" aria-label="Doctor portrait"></div><h4>Lorem ipsum</h4><p class="role">Endocrinologists</p><p>Lorem ipsum dolor sit amet, consectetur adipiscing elit. Accumsan felis tempus nascetur.</p><span class="more">Read More</span></div>
    <div class="doc"><div class="face" role="img" aria-label="Doctor portrait"></div><h4>Lorem ipsum</h4><p class="role">Neurologists</p><p>Lorem ipsum dolor sit amet, consectetur adipiscing elit. Accumsan felis tempus nascetur.</p><span class="more">Read More</span></div>
    <div class="doc"><div class="face" role="img" aria-label="Doctor portrait"></div><h4>Lorem ipsum</h4><p class="role">Gynecologists</p><p>Lorem ipsum dolor sit amet, consectetur adipiscing elit. Accumsan felis tempus nascetur.</p><span class="more">Read More</span></div>
    <div class="doc"><div class="face" role="img" aria-label="Doctor portrait"></div><h4>Lorem ipsum</h4><p class="role">Oncologists</p><p>Lorem ipsum dolor sit amet, consectetur adipiscing elit. Accumsan felis tempus nascetur.</p><span class="more">Read More</span></div>
    <div class="doc"><div class="face" role="img" aria-label="Doctor portrait"></div><h4>Lorem ipsum</h4><p class="role">Urologists</p><p>Lorem ipsum dolor sit amet, consectetur adipiscing elit. Accumsan felis tempus nascetur.</p><span class="more">Read More</span></div>
  </div>
</section>

<section class="news">
  <svg class="abs" style="left:586px;top:26px" width="28" height="28" viewBox="0 0 26 26"><rect x="9" y="1" width="8" height="24" fill="#fff" opacity=".7"/><rect x="1" y="9" width="24" height="8" fill="#fff" opacity=".5"/></svg>
  <h2>Our Latest News</h2>
  <p class="sub">Lorem ipsum dolor sit amet, consectetur adipiscing elit. Donec rhoncus diam sit elementum vulputate dignissim.</p>
  <div class="news-grid">
    <div class="news-item"><div class="news-img" role="img" aria-label="Masked clinician holding a test swab" style="background:linear-gradient(150deg,#e9eef2,#a9bccb)"></div><h3>Lorem ipsum</h3><p>Contrary to popular belief, Lorem Ipsum is not simply random text. It has roots in a piece of classical literature from 45 BC, making it over 2000 years old.</p><span class="rm">Read More</span></div>
    <div class="news-item"><div class="news-img" role="img" aria-label="Surgical team in an operating room" style="background:linear-gradient(150deg,#9fc1d6,#3f6f93)"></div><h3>Lorem ipsum</h3><p>Many desktop publishing packages and web page editors now use Lorem Ipsum as their default model text, and many web sites still in their infancy.</p><span class="rm">Read More</span></div>
    <div class="news-item"><div class="news-img" role="img" aria-label="Hospital corridor with medical staff" style="background:linear-gradient(150deg,#e4e7ec,#8fa0b8)"></div><h3>Lorem ipsum</h3><p>Contrary to popular belief, Lorem Ipsum is not simply random text. It has roots in a piece of classical literature from 45 BC, making it old.</p><span class="rm">Read More</span></div>
  </div>
</section>

<section class="appointment">
  <div class="appt-photo" role="img" aria-label="Doctor consulting with a patient across a desk"></div>
  <div class="appt-card">
    <svg class="corner" width="70" height="70" viewBox="0 0 70 70"><path d="M70 0V70L0 0z" fill="var(--pink)" opacity=".9"/><path d="M70 0V40L30 0z" fill="var(--purple)"/></svg>
    <p class="label">Book appointment</p>
    <h2>We are here for you</h2>
    <div class="fields">
      <div class="field"><span class="fi"></span>Enter Your Name</div>
      <div class="field"><span class="fi"></span>Enter Your Email</div>
      <div class="field"><span class="fi"></span>Nephrologists ▾</div>
      <div class="field"><span class="fi"></span>Enter Your Phone</div>
    </div>
    <span class="btn">MAKE APPOINTMENT ›</span>
  </div>
</section>

<footer class="site-footer">
  <div class="foot-cols">
    <div class="foot-brand">
      <div class="brand"><span class="dot"></span>Wellspring Crest</div>
      <p>Lorem ipsum dolor sit amet, consectetur adipiscing elit. Donec rhoncus diam sit elementum vulputate dignissim ipsum dolor sit amet.</p>
    </div>
    <div><h4>DEPARTMENTS</h4><ul><li>Surgery and Radiology</li><li>Family</li><li>Gynecology</li><li>Dermatology</li><li>X-ray</li></ul></div>
    <div><h4>LINKS</h4><ul><li>About Us</li><li>Services</li><li>Our Team</li><li>Contact</li></ul></div>
    <div><h4>Services</h4><ul><li>Outpatient Surgery</li><li>Cardiac</li><li>Dermatological</li><li>Transportation</li></ul></div>
    <div class="contact"><h4>CONTACT US</h4><ul><li><i></i>(305) 555-0142</li><li><i></i>hello@bluefernclinicmiami.org</li><li><i></i>Miami, Florida</li></ul><div class="socials"><span></span><span></span><span></span><span></span></div></div>
  </div>
  <div class="copyright">© 2020 bluefernclinicmiami.org. All rights reserved.</div>
</footer>

</body>
</html>
```